Plovrent Website Design - Wordpress

Need a website WordPress design for our existing website that we just stood up. The logo is already in place and name. Plovrent.com We are a company which makes connections with our clients through educating them and providing networking events. We would like for the website to show a VIP/special feel to it.

Target Market(s)

Business executives and employees. Age group 26-65 in the following sectors:
- Technology
- Human Resources
- Finance
- Sales

Industry/Entity Type

Technical Service

Number of Pages Required

4 page

Font styles to use
Sans Serif

Requirements
Must have
• Must be something for Wordpress
Nice to have
• Would like this to be professional but look cutting edge and VIP.

```html
<!DOCTYPE html>
<html lang="en">
<head>
<meta charset="utf-8">
<title>Plovrent</title>
<link href="https://fonts.googleapis.com/css2?family=Lato:wght@400;700;900&display=swap" rel="stylesheet">
<style>
:root{
  --yellow:#e8a317;
  --blue:#1d5f9e;
  --red:#c3161d;
  --purple:#6a2c86;
  --green:#3aa83f;
  --ink:#ffffff;
  --bg-dark:#1e1e1e;
  --bg-black:#060606;
  --bg-mid:#262626;
  --night:#0c1226;
}
*{margin:0;padding:0;box-sizing:border-box}
html,body{width:1200px;height:4045px;overflow:hidden;background:var(--bg-black)}
body{font-family:"Lato",sans-serif;color:var(--ink)}
.page{position:relative;width:1200px;height:4045px;overflow:hidden}
.abs{position:absolute}
.center{left:0;width:1200px;text-align:center}

/* hero */
.hero{top:0;left:0;width:1200px;height:760px;background:radial-gradient(ellipse at 55% 40%,#3b4468 0%,#1a2140 35%,var(--night) 70%,#05070f 100%)}
.brand{top:46px;left:113px;display:flex;align-items:center;gap:18px}
.brand-square{width:58px;height:58px;background:var(--yellow)}
.brand-name{font-size:40px;font-weight:700;letter-spacing:4px;color:var(--ink)}
.nav{top:68px;left:618px;display:flex;gap:0;font-size:17px;font-weight:700;letter-spacing:1px}
.nav span{position:absolute;white-space:nowrap}
.hero-title{top:296px;font-size:54px;font-weight:700;letter-spacing:5px}
.hero-btn{top:442px;left:507px;width:186px;height:58px;border:3px solid var(--yellow);color:var(--yellow);font-size:18px;font-weight:700;letter-spacing:2px;line-height:52px;text-align:center}
.slider-arrow{top:345px}

/* strategy */
.strategy{top:640px;left:0;width:1200px;height:965px;background:var(--bg-dark)}
.section-title{font-size:31px;font-weight:700;letter-spacing:3px}
.lead{font-size:20px;line-height:48px;letter-spacing:1.5px}
.trait{font-size:28px;letter-spacing:2px;line-height:1}
.trait small{display:block;font-size:26px;margin-bottom:16px;font-weight:400}
.trait.left{text-align:right;right:822px}
.trait.right{left:815px}

/* offer */
.offer{top:1605px;left:0;width:1200px;height:700px;background:var(--bg-black)}
.offer-card{top:1861px;width:216px;height:189px;border:3px solid var(--ink);padding:66px 16px 0 16px;font-size:13.5px;line-height:17px;letter-spacing:.5px}
.offer-icon{top:1820px}
.value-btn{top:2133px;left:483px;width:191px;height:65px;border-radius:8px;background:var(--yellow);box-shadow:0 0 18px rgba(232,163,23,.55);font-size:21px;font-weight:700;line-height:65px;text-align:center}

/* unique */
.unique{top:2265px;left:0;width:1200px;height:740px;background:var(--bg-mid)}
.unique-title{top:2470px;font-size:52px;font-weight:700;letter-spacing:4px;color:var(--red)}
.values{top:2572px;font-size:32px;letter-spacing:2px}
.unique-copy{top:2638px;left:248px;width:710px;text-align:center;font-size:18px;line-height:31px;letter-spacing:1px}

/* team */
.team{top:2940px;left:0;width:1200px;height:640px;background:var(--bg-black)}
.portrait-frame{width:230px;height:236px;border:4px solid var(--green)}
.portrait{width:230px;height:236px;background:linear-gradient(160deg,#e6e6e6 0%,#9a9a9a 45%,#2a2a2a 100%)}
.bio{top:3356px;width:420px;text-align:center;font-size:18px;line-height:32px;letter-spacing:1px}

/* footer */
.footer{top:3560px;left:0;width:1200px;height:445px;background:var(--bg-dark)}
.footer-title{font-size:28px;font-weight:700;letter-spacing:2px}
.contact-line{font-size:16px;letter-spacing:1px;display:flex;align-items:center;gap:10px}
.meetup-banner{top:3770px;left:442px;width:278px;height:119px;background:linear-gradient(100deg,var(--blue) 0%,var(--purple) 35%,var(--red) 70%,var(--yellow) 100%)}
.search-box{top:3781px;left:828px;width:270px;height:44px;border:2px solid var(--green);border-radius:6px;font-size:15px;font-style:italic;color:#9a9a9a;padding:11px 0 0 20px}
.social{top:3858px;width:36px;height:36px;border-radius:50%;background:var(--ink)}
.footer-nav{top:3936px;font-size:15px;letter-spacing:1px}
.copyright{top:4005px;left:0;width:1200px;height:40px;background:var(--bg-black);font-size:14px;line-height:40px;text-align:center;letter-spacing:.5px}
</style>
</head>
<body>
<div class="page">

  <!-- hero -->
  <section class="abs hero" role="img" aria-label="Night sky with the milky way above a person standing on a hilltop"></section>
  <svg class="abs" style="top:560px;left:0" width="1200" height="220" viewBox="0 0 1200 220">
    <polygon points="0,80 790,200 1200,80 1200,220 0,220" fill="#1e1e1e"/>
    <polygon points="0,68 790,188 1200,80 1200,92 790,200 0,80" fill="#e8a317"/>
  </svg>
  <div class="abs brand">
    <div class="brand-square"></div>
    <div class="brand-name">PLOVRENT</div>
  </div>
  <nav class="abs nav">
    <span style="left:0">EVENTS</span>
    <span style="left:110px">EXPAND</span>
    <span style="left:232px">X</span>
    <span style="left:275px">ABOUT</span>
    <span style="left:377px">CONNECT</span>
  </nav>
  <h1 class="abs center hero-title">EXPAND YOUR BUSINESS</h1>
  <div class="abs hero-btn">LEARN MORE</div>
  <svg class="abs slider-arrow" style="left:70px" width="26" height="50" viewBox="0 0 26 50"><polyline points="24,2 2,25 24,48" fill="none" stroke="#fff" stroke-width="3"/></svg>
  <svg class="abs slider-arrow" style="left:1104px" width="26" height="50" viewBox="0 0 26 50"><polyline points="2,2 24,25 2,48" fill="none" stroke="#fff" stroke-width="3"/></svg>

  <!-- strategy -->
  <section class="abs strategy"></section>
  <h2 class="abs center section-title" style="top:846px">IT'S ABOUT OUR UNIQUE X STRATEGY</h2>
  <p class="abs center lead" style="top:923px">PLOVRENT provides impactful connection opportunities to help educate,<br>equip and expand you and your business</p>
  <svg class="abs" style="top:1092px;left:445px" width="312" height="316" viewBox="0 0 312 316">
    <circle cx="156" cy="158" r="150" fill="#2c2c2c"/>
  </svg>
  <div class="abs trait left" style="top:1150px;color:var(--ink)"><small style="color:var(--blue)">MIND</small>THOUGHT</div>
  <div class="abs trait left" style="top:1282px"><small style="color:var(--purple)">SOUL</small>INTUITION</div>
  <div class="abs trait right" style="top:1150px"><small style="color:var(--red)">HEART</small>EMOTIONS</div>
  <div class="abs trait right" style="top:1282px"><small style="color:var(--yellow)">STRENGTH</small>ENERGY</div>

  <!-- offer -->
  <section class="abs offer"></section>
  <h2 class="abs center section-title" style="top:1688px;font-size:29px">WHAT WE OFFER YOU</h2>

  <div class="abs offer-card" style="left:102px">At PLOVRENT, we provide effective training and learning as the foundation for building a healthy, successful company.</div>
  <div class="abs offer-card" style="left:361px">Through our connected ecosystem of companies, we'll help find the right partners for equipping you to move forward.</div>
  <div class="abs offer-card" style="left:620px">We connect you with others who have successfully implemented our X Strategy to facilitate growth in their business.</div>
  <div class="abs offer-card" style="left:879px">Our goal is to help you and your business increase productivity and scale through effective strategy and healthy culture.</div>

  <svg class="abs offer-icon" style="left:172px" width="80" height="80" viewBox="0 0 80 80">
    <circle cx="40" cy="40" r="37" fill="#060606" stroke="#fff" stroke-width="3"/>
    <rect x="22" y="22" width="36" height="24" fill="none" stroke="#fff" stroke-width="2.5"/>
    <polyline points="27,40 35,33 42,37 52,27" fill="none" stroke="#fff" stroke-width="2.5"/>
    <line x1="40" y1="46" x2="40" y2="58" stroke="#fff" stroke-width="2.5"/>
    <line x1="30" y1="58" x2="50" y2="58" stroke="#fff" stroke-width="2.5"/>
  </svg>
  <svg class="abs offer-icon" style="left:431px" width="80" height="80" viewBox="0 0 80 80">
    <circle cx="40" cy="40" r="37" fill="#060606" stroke="#fff" stroke-width="3"/>
    <line x1="34" y1="20" x2="34" y2="30" stroke="#fff" stroke-width="2.5"/>
    <line x1="46" y1="20" x2="46" y2="30" stroke="#fff" stroke-width="2.5"/>
    <path d="M27 30 H53 V40 Q53 50 40 50 Q27 50 27 40 Z" fill="none" stroke="#fff" stroke-width="2.5"/>
    <line x1="40" y1="50" x2="40" y2="60" stroke="#fff" stroke-width="2.5"/>
  </svg>
  <svg class="abs offer-icon" style="left:690px" width="80" height="80" viewBox="0 0 80 80">
    <circle cx="40" cy="40" r="37" fill="#060606" stroke="#fff" stroke-width="3"/>
    <polyline points="22,32 54,32" fill="none" stroke="#fff" stroke-width="3"/>
    <polyline points="46,24 55,32 46,40" fill="none" stroke="#fff" stroke-width="3"/>
    <polyline points="58,48 26,48" fill="none" stroke="#fff" stroke-width="3"/>
    <polyline points="34,40 25,48 34,56" fill="none" stroke="#fff" stroke-width="3"/>
  </svg>
  <svg class="abs offer-icon" style="left:949px" width="80" height="80" viewBox="0 0 80 80">
    <circle cx="40" cy="40" r="37" fill="#060606" stroke="#fff" stroke-width="3"/>
    <rect x="26" y="22" width="28" height="36" fill="none" stroke="#fff" stroke-width="2.5"/>
    <line x1="33" y1="30" x2="33" y2="50" stroke="#fff" stroke-width="2.5"/>
    <line x1="40" y1="30" x2="40" y2="50" stroke="#fff" stroke-width="2.5"/>
    <line x1="47" y1="30" x2="47" y2="50" stroke="#fff" stroke-width="2.5"/>
  </svg>

  <div class="abs value-btn">X= Value</div>

  <!-- unique -->
  <section class="abs unique"></section>
  <svg class="abs" style="top:2230px;left:0" width="1200" height="170" viewBox="0 0 1200 170">
    <polygon points="0,0 1200,0 1200,10 1080,160 480,85 0,85" fill="#060606"/>
    <polygon points="480,85 1080,160 1200,10 1200,30 1080,180 480,97" fill="#6a2c86"/>
  </svg>
  <h2 class="abs center unique-title">X = UNIQUE</h2>
  <p class="abs center values">Virtue | Appreciation | Respect | Ownership</p>
  <p class="abs unique-copy">Our team is an unusual mix. We're globally experienced, technically capable, community focussed and highly fruitful. The four core values above inform everything we do. Our special sauce is knowing how to fuse structure and productivity with relationship and creativity.</p>

  <!-- team -->
  <section class="abs team"></section>
  <svg class="abs" style="top:2860px;left:0" width="1200" height="140" viewBox="0 0 1200 140">
    <polygon points="0,0 162,125 1200,66 1200,140 0,140" fill="#060606"/>
    <polygon points="0,0 162,125 1200,66 1200,80 162,140 0,16" fill="#e8a317"/>
  </svg>

  <div class="abs portrait-frame" style="top:3080px;left:256px"></div>
  <div class="abs portrait" style="top:3088px;left:248px" role="img" aria-label="Black and white portrait of Marcel Doverin"></div>
  <div class="abs portrait-frame" style="top:3080px;left:758px"></div>
  <div class="abs portrait" style="top:3088px;left:750px" role="img" aria-label="Black and white portrait of Adrian Kellow"></div>

  <p class="abs bio" style="left:151px">Marcel Doverin has lived and worked in several countries, experiencing varied cultures and companies.</p>
  <p class="abs bio" style="left:653px">Adrian Kellow is highly experienced as an entrepreneur, business owner and marketing expert.</p>

  <svg class="abs" style="top:3472px;left:350px" width="36" height="36" viewBox="0 0 36 36">
    <circle cx="18" cy="18" r="16" fill="none" stroke="#3aa83f" stroke-width="2.5"/>
    <line x1="10" y1="18" x2="25" y2="18" stroke="#3aa83f" stroke-width="2.5"/>
    <polyline points="19,12 25,18 19,24" fill="none" stroke="#3aa83f" stroke-width="2.5"/>
  </svg>
  <svg class="abs" style="top:3472px;left:863px" width="36" height="36" viewBox="0 0 36 36">
    <circle cx="18" cy="18" r="16" fill="none" stroke="#3aa83f" stroke-width="2.5"/>
    <line x1="10" y1="18" x2="25" y2="18" stroke="#3aa83f" stroke-width="2.5"/>
    <polyline points="19,12 25,18 19,24" fill="none" stroke="#3aa83f" stroke-width="2.5"/>
  </svg>

  <!-- footer -->
  <section class="abs footer"></section>
  <svg class="abs" style="top:3490px;left:0" width="1200" height="100" viewBox="0 0 1200 100">
    <polygon points="0,20 540,50 1060,90 1200,0 1200,100 0,100" fill="#1e1e1e"/>
    <polygon points="540,40 1060,80 1200,-5 1200,12 1060,96 540,54" fill="#1d5f9e"/>
  </svg>

  <h3 class="abs footer-title" style="top:3724px;left:138px">CONTACT US</h3>
  <div class="abs contact-line" style="top:3777px;left:138px">
    <svg width="16" height="16" viewBox="0 0 16 16"><path d="M3 1 L6 1 L7 5 L5 6.5 Q6.5 9.5 9.5 11 L11 9 L15 10 L15 13 Q15 15 13 15 Q2 14 1 3 Q1 1 3 1 Z" fill="#e8a317"/></svg>
    1-855-PLOVRN1
  </div>
  <div class="abs contact-line" style="top:3820px;left:138px">
    <svg width="16" height="12" viewBox="0 0 16 12"><rect x="0" y="0" width="16" height="12" fill="#c3161d"/><polyline points="0,0 8,7 16,0" fill="none" stroke="#1e1e1e" stroke-width="1.5"/></svg>
    CONNECT@PLOVRENT.COM
  </div>

  <h3 class="abs footer-title" style="top:3720px;left:445px">MEET UP</h3>
  <div class="abs meetup-banner" role="img" aria-label="Event banner for an Expand Your Business meetup"></div>

  <h3 class="abs footer-title" style="top:3720px;left:823px">SEARCH</h3>
  <div class="abs search-box">Search</div>
  <svg class="abs" style="top:3792px;left:1060px" width="22" height="22" viewBox="0 0 22 22">
    <circle cx="9" cy="9" r="6.5" fill="none" stroke="#3aa83f" stroke-width="2.5"/>
    <line x1="14" y1="14" x2="20" y2="20" stroke="#3aa83f" stroke-width="2.5"/>
  </svg>
  <div class="abs social" style="left:883px"></div>
  <div class="abs social" style="left:931px"></div>
  <div class="abs social" style="left:980px"></div>

  <p class="abs center footer-nav">EVENTS &nbsp;| &nbsp;EXPAND &nbsp;| &nbsp;X &nbsp;| &nbsp;ABOUT &nbsp;| &nbsp;CONNECT</p>
  <div class="abs copyright">Copyrights 2019. All rights reserved</div>

</div>
</body>
</html>
```